Title: Iron Lantern Sub: Rivers carry every morning west - Book cover

I need a complete book cover, front, spine, and back.

Religions Book

This book is more about the Title so it should be strong and serious.

Like the color Deep Red and black, blue. Deep purple
Avoid greens, orange, yellows.

Maybe a picture of a strong hand on the Bible. OR someone yelling.

If any pictures are used they must be 100% royalty free with proof or a buyout of image.

I have attached a couple of designs that the client likes. Just as a reference. The exception they DIDN'T like the pictures in the book cover.

Please ask any questions to clarify.

Please see the file I just uploaded called 'Book Cover samples.png" The clients likes the Title: Copper Vale" the best. Please create a design something closer to this. The like how the title jumps off the page with a 2D look.

Again the Title must standout, and any use of images must be a secondary to the design.

I am happy with we the designs that have been submitted so far.

I hope this helps you get closer.

Thank you

First of all I want to thank you for all of your designs. At the beginning the client thought he would like a picture that represented the title. But after looking at all of the designs. He has now decided NOT to have any pictures.

Here is what he wants

1. BOLD Font (San Serif only) no fancy versions for the Title "IRON LANTERN" in uppercase. The title font should have some dimension to it to appear 2D or 3D looks. Shiny look. It needs to looks like it jumping off the page.

2. The subtitle right below the title in San Serif font)

3. Background solid color either black, dark red, or dark blue. The background can be slightly textured or gradation fill, etc.

4. The cover must have a strong and bold statement.

Thank you again.

Please use this photo on the back cover.

Thank you

• A picture that over powers the Title.

```html
<!DOCTYPE html>
<html lang="en">
<head>
<meta charset="utf-8">
<title>Iron Lantern – Book Cover Wrap</title>
<link rel="stylesheet" href="https://fonts.googleapis.com/css2?family=Open+Sans:wght@400;600;700&family=Share+Tech+Mono&display=swap">
<style>
  :root {
    --ink-black: #070606;
    --glow-red: #a30404;
    --title-red: #7a0d0d;
    --subtitle-red: #6a0c0c;
    --spine-red: #c4100f;
    --author-ink: #140909;
    --bevel-light: rgba(255, 95, 95, 0.6);
    --bevel-dark: #000;
  }
  * { margin: 0; padding: 0; box-sizing: border-box; }
  html, body {
    width: 1200px;
    height: 864px;
    overflow: hidden;
    background: var(--ink-black);
  }
  .cover-wrap {
    position: relative;
    width: 1200px;
    height: 864px;
    overflow: hidden;
  }

  /* Back cover */
  .back-cover {
    position: absolute;
    left: 0; top: 0;
    width: 577px; height: 864px;
    background:
      radial-gradient(circle at 60px 790px, var(--glow-red) 0, rgba(140,0,0,0.75) 90px, rgba(90,0,0,0.35) 220px, transparent 380px),
      linear-gradient(to bottom, #050505 0%, #0a0505 35%, #2a0404 75%, #3c0505 100%);
  }

  /* Spine */
  .spine {
    position: absolute;
    left: 577px; top: 0;
    width: 55px; height: 864px;
    background: linear-gradient(to right, #0b0707, #080606 50%, #0b0707);
  }
  .spine-text {
    position: absolute;
    left: 50%;
    bottom: 22px;
    transform: translateX(-50%) rotate(180deg);
    writing-mode: vertical-rl;
    white-space: nowrap;
    color: var(--spine-red);
    line-height: 1;
  }
  .spine-author {
    font-family: "Share Tech Mono", monospace;
    font-size: 22px;
    letter-spacing: 0.3em;
    text-transform: uppercase;
  }
  .spine-title {
    font-family: "Open Sans", sans-serif;
    font-size: 22px;
    margin-top: 16px;
  }

  /* Front cover */
  .front-cover {
    position: absolute;
    left: 632px; top: 0;
    width: 568px; height: 864px;
    background:
      radial-gradient(circle at 540px 20px, var(--glow-red) 0, rgba(140,0,0,0.8) 70px, rgba(90,0,0,0.4) 200px, transparent 360px),
      linear-gradient(to bottom, #3a0505 0%, #1a0303 30%, #090505 65%, #050505 100%);
  }
  .author-name {
    position: absolute;
    left: 0; right: 0;
    top: 62px;
    padding-left: 20px;
    text-align: center;
    font-family: "Share Tech Mono", monospace;
    font-size: 50px;
    letter-spacing: 0.3em;
    line-height: 80px;
    text-transform: uppercase;
    color: var(--author-ink);
    text-shadow:
      1px 1px 0 var(--bevel-light),
      2px 2px 1px rgba(255, 70, 70, 0.3),
      -1px -1px 0 var(--bevel-dark);
  }
  .author-name span { display: block; }

  .title-block {
    position: absolute;
    left: 0; right: 0;
    top: 660px;
    text-align: center;
    font-family: "Open Sans", sans-serif;
  }
  .book-title {
    font-size: 66px;
    font-weight: 700;
    line-height: 1.1;
    color: var(--title-red);
    text-shadow:
      -1px -1px 0 var(--bevel-light),
      1px 1px 0 #2a0000,
      2px 2px 0 #1a0000,
      3px 3px 0 #0c0000,
      4px 5px 8px rgba(0,0,0,0.95);
  }
  .book-subtitle {
    margin-top: 22px;
    font-size: 33px;
    font-weight: 600;
    line-height: 1.1;
    color: var(--subtitle-red);
    text-shadow:
      -1px -1px 0 var(--bevel-light),
      1px 1px 0 #1a0000,
      2px 2px 0 #0c0000,
      3px 4px 6px rgba(0,0,0,0.9);
  }
</style>
</head>
<body>
<main class="cover-wrap">
  <section class="back-cover" aria-label="Back cover"></section>

  <section class="spine" aria-label="Spine">
    <div class="spine-text">
      <span class="spine-author">Mara Keswick</span><span class="spine-title">Iron Lantern&nbsp; Rivers carry every morning west</span>
    </div>
  </section>

  <section class="front-cover" aria-label="Front cover">
    <p class="author-name"><span>Mara</span><span>Keswick</span></p>
    <header class="title-block">
      <h1 class="book-title">IRON LANTERN</h1>
      <p class="book-subtitle">Rivers carry every morning west</p>
    </header>
  </section>
</main>
</body>
</html>
```